Bright Harbor Capital website

Build a website template for the Bright Harbor Capital fund.
Looking for a cool website design showing companies we are using the latest in web design trends. We want to attract app developers, typically the younger set.
A good example of one of our competitive firms is http://tallmeadowfund.example
The required components for the website include:
1) Funding application
2) about our firm
a) Partner profiles - We will include photographs and bios about each of the partners in our firm.
b) Invest with Bright Harbor - This will include information how to invest with our fund
c) our process - About our process for evaluating, funding and helping build successful businesses - This will include a narrative about the target companies, how we work, the type of deals we are interested in, our expectations, etc ...
3) Investment profiles - Stories about the companies we invest with
4) News - Output from our twitter feed and copies of our Blog posts

```html
<!DOCTYPE html>
<html lang="en">
<head>
<meta charset="utf-8">
<title>Bright Harbor Capital</title>
<link href="https://fonts.googleapis.com/css2?family=Open+Sans:wght@400;600&display=swap" rel="stylesheet">
<style>
:root{
  --green:#5c9e0e;
  --green-btn:#5fae0a;
  --ink:#2b2b2b;
  --text:#8a8a8a;
  --muted:#a9a9a9;
  --nav:#333333;
  --panel:#f2f2f2;
  --form:#e4e4e4;
  --footer:#2b2b2b;
  --footer-bottom:#1f1f1f;
  --footer-text:#8f8f8f;
  --white:#ffffff;
}
*{box-sizing:border-box;margin:0;padding:0}
html,body{width:827px;height:1200px;overflow:hidden;background:var(--white)}
body{font-family:"Open Sans",Arial,sans-serif;color:var(--text);position:relative}
.page{position:relative;width:827px;height:1200px;overflow:hidden}
.abs{position:absolute}
.topline{left:0;top:0;width:827px;height:2.4px;background:var(--green)}
.brand{left:97px;top:26px;color:var(--green);font-size:20px;font-weight:600;letter-spacing:-.3px;line-height:1;white-space:nowrap}
.callus{left:460px;top:34px;font-size:9px;color:var(--muted);display:flex;align-items:center;gap:4px}
.callus strong{font-weight:400;font-size:11px}
.social{display:flex;gap:3.6px}
.social span{width:15px;height:15px;border-radius:50%;background:#d6d6d6;display:block}
.social.head{left:592px;top:32px}
.social.foot{left:588px;top:1142px}
.social.foot span{background:#4a4a4a}
.navbar{left:0;top:72px;width:827px;height:31px;background:var(--nav)}
.navbar ul{list-style:none;display:flex;position:absolute;left:97px;top:9px;font-size:8.8px;color:#b5b5b5}
.navbar li{padding:0 6px;border-left:1px solid #4a4a4a;line-height:1.3}
.navbar li:first-child{padding-left:0;border:0;color:var(--white)}
.search{left:592px;top:79px;width:126px;height:17px;border-radius:5px;background:#f0f0f0;font-size:8.5px;color:#aaa;padding:2px 8px}
.search svg{position:absolute;right:6px;top:3px}
.hero-bg{left:0;top:103px;width:827px;height:269px;background:linear-gradient(90deg,#d4d8dc 0%,#c9cdd1 35%,#e4e7ea 70%,#eef0f2 100%)}
.hero-photo{left:396px;top:103px;width:330px;height:269px;background:linear-gradient(180deg,rgba(214,184,150,.55) 0%,rgba(196,160,124,.6) 45%,rgba(70,70,74,.75) 80%,rgba(50,50,54,.8) 100%)}
.hero-title{left:98px;top:160px;font-size:18px;font-weight:400;color:var(--ink);line-height:21px;white-space:nowrap}
.hero-copy{left:97px;top:216px;width:200px;font-size:11px;line-height:13.3px;color:#3a3a3a}
.btn-dark{left:97px;top:284px;width:91px;height:26px;background:#333;color:#fff;font-size:11px;border-radius:2px;display:flex;align-items:center;justify-content:center;box-shadow:0 2px 0 #111}
.dots{left:97px;top:323px;display:flex;gap:2px}
.dots span{width:6px;height:6px;border-radius:50%;background:var(--green)}
.dots span:first-child{background:#222}
.features{left:0;top:372px;width:827px;height:194px;background:var(--panel)}
.feat-icon{width:39px;height:39px;border-radius:50%;background:#fff;box-shadow:0 1px 2px rgba(0,0,0,.12);display:flex;align-items:center;justify-content:center}
.feat-title{font-size:10.5px;color:var(--ink)}
.feat-text{font-size:8.4px;line-height:11.7px;color:var(--text);width:165px}
.btn-line{height:19px;border:1px solid #9a9a9a;background:#fff;font-size:8px;color:#333;display:flex;align-items:center;justify-content:center;width:59px}
.section-title{font-size:10.5px;color:var(--ink);font-weight:400}
.photo{background:linear-gradient(135deg,#c8d6e6,#7d9dc4)}
.photo.meeting{background:linear-gradient(135deg,#d9dde2,#6d7380)}
.body-copy{font-size:8.4px;line-height:11.6px;color:var(--text)}
.form{left:541px;top:620px;width:189px;height:191px;background:var(--form);border:1px solid #dadada;padding:8px 12px}
.form h3{font-size:10px;font-weight:400;color:var(--ink)}
.form p{font-size:8.2px;line-height:13px;color:var(--muted);margin-top:3px}
.field{background:#fff;border:1px solid #d0d0d0;font-size:8px;color:#aaa;padding:1px 3px;height:15px;margin-top:6px}
.field.area{height:47px;margin-top:4px}
.submit{position:absolute;right:12px;top:169px;width:69px;height:16px;background:var(--green-btn);color:#fff;font-size:8.5px;display:flex;align-items:center;justify-content:center}
.avatar-warm{background:linear-gradient(135deg,#e7c9a8,#a27556)}
.avatar-cool{background:linear-gradient(135deg,#c9d6e0,#6e7f8c)}
.name{color:var(--green);font-size:10px}
.footer{left:0;top:979px;width:827px;height:197px;background:var(--footer);border-top:2.4px solid var(--green)}
.footer-bottom{left:0;top:1176px;width:827px;height:24px;background:var(--footer-bottom);font-size:7.5px;color:#ddd;text-align:center;line-height:24px}
.f-title{font-size:10.5px;color:#fff}
.f-text{font-size:8.2px;line-height:13px;color:var(--footer-text)}
.f-links{list-style:none;font-size:8.2px;line-height:16.2px;color:var(--footer-text)}
.f-links li:first-child{color:var(--green)}
.f-brand{font-size:13px;font-weight:600;color:#fff;white-space:nowrap}
.f-mark{width:20px;height:20px;border-radius:50%;background:#fff}
.contact{font-size:8.4px;line-height:13px;color:#bdbdbd}
</style>
</head>
<body>
<div class="page">
  <div class="abs topline"></div>

  <header>
    <div class="abs brand">Bright Harbor Capital</div>
    <div class="abs callus">
      <svg width="9" height="9" viewBox="0 0 10 10"><path d="M2 1l2 2-1 1.3c.6 1.2 1.5 2.1 2.7 2.7L7 6l2 2-1.2 1.3C4.5 9 1 5.5.7 2.2z" fill="#b5b5b5"/></svg>
      Call Us <strong>+1555 01234</strong>
    </div>
    <div class="abs social head"><span></span><span></span><span></span><span></span><span></span><span></span><span></span></div>
  </header>

  <nav class="abs navbar">
    <ul>
      <li>Home</li><li>Funding application</li><li>About our firm</li><li>Partner profiles</li><li>Our process</li><li>Investment profiles</li><li>Contact us</li>
    </ul>
  </nav>
  <div class="abs search">Search
    <svg width="11" height="11" viewBox="0 0 12 12"><circle cx="7" cy="5" r="3.6" fill="none" stroke="#555" stroke-width="1.5"/><path d="M4.3 7.7L1 11" stroke="#555" stroke-width="1.8"/></svg>
  </div>

  <section>
    <div class="abs hero-bg" role="img" aria-label="Blurred office corridor with business people walking"></div>
    <div class="abs hero-photo" role="img" aria-label="Portrait photo of a smiling businesswoman in a dark blazer"></div>
    <h1 class="abs hero-title">Funding and helping<br>build successful businesses</h1>
    <p class="abs hero-copy">This will include a narrative about the target companies, how we work, the type of deals we are interested in, our expectations, etc ...</p>
    <div class="abs btn-dark">READ MORE</div>
    <div class="abs dots"><span></span><span></span><span></span></div>
  </section>

  <section class="abs features"></section>
  <div class="abs feat-icon" style="left:98px;top:426px">
    <svg width="22" height="20" viewBox="0 0 22 20"><rect x="1" y="1" width="20" height="13" fill="none" stroke="var(--green)" stroke-width="1.6"/><rect x="3" y="3" width="16" height="9" fill="var(--green)"/><rect x="9" y="15" width="4" height="2" fill="var(--green)"/><rect x="6" y="17" width="10" height="1.6" fill="var(--green)"/></svg>
  </div>
  <div class="abs feat-title" style="left:143px;top:433px">About Our Process For Evaluating</div>
  <p class="abs feat-text" style="left:143px;top:456px">Lorem ipsum dolor sit amet, consectetur adipisicing elit, sed do eiusmod tempor incididunt ut labore et dolore magna aliqua.</p>
  <div class="abs btn-line" style="left:143px;top:514px">Learn More</div>

  <div class="abs feat-icon" style="left:332px;top:426px">
    <svg width="24" height="20" viewBox="0 0 24 20"><path d="M12 1l10 5-10 5L2 6z" fill="var(--green)"/><path d="M2 10l10 5 10-5" fill="none" stroke="var(--green)" stroke-width="2"/><path d="M2 14l10 5 10-5" fill="none" stroke="var(--green)" stroke-width="2"/></svg>
  </div>
  <div class="abs feat-title" style="left:378px;top:433px">Funding And Helping</div>
  <p class="abs feat-text" style="left:378px;top:456px;width:130px">Lorem ipsum dolor sit amet, consectetur adipisicing elit, sed do eiusmod tempor incididunt ut labore et dolore magna aliqua.</p>
  <div class="abs btn-line" style="left:378px;top:514px">Learn More</div>

  <div class="abs feat-icon" style="left:526px;top:426px">
    <svg width="22" height="22" viewBox="0 0 22 22"><path d="M11 1l9 5v10l-9 5-9-5V6z" fill="#7fc21e"/><path d="M2 6l9 5 9-5M11 11v10" fill="none" stroke="#fff" stroke-width="1.2"/></svg>
  </div>
  <div class="abs feat-title" style="left:570px;top:433px">Our Expectations</div>
  <p class="abs feat-text" style="left:570px;top:456px">Lorem ipsum dolor sit amet, consectetur adipisicing elit, sed do eiusmod tempor incididunt ut labore et dolore magna aliqua.</p>
  <div class="abs btn-line" style="left:570px;top:514px">Learn More</div>

  <section>
    <h2 class="abs section-title" style="left:98px;top:597px">Our Process</h2>
    <div class="abs photo" style="left:100px;top:626px;width:155px;height:89px" role="img" aria-label="Businessman facing a chalk sketch of team, product and company ideas"></div>
    <p class="abs body-copy" style="left:262px;top:624px;width:212px">Lorem ipsum dolor sit amet, consectetur adipisicing elit, sed do eiusmod tempor incididunt ut labore et dolore magna aliqua.Ut enim ad minim veniam, quis nostrud exercitation ullamco laboris nisi ut aliquip ex ea commodo consequat. Duis aute irure dolor in reprehenderit in voluptate velit esse cillum dolore eu fugiat nulla pariatur. Excepteur sint occaecat</p>
    <div class="abs photo meeting" style="left:100px;top:729px;width:155px;height:88px" role="img" aria-label="Business team meeting around a table with laptops"></div>
    <p class="abs body-copy" style="left:262px;top:727px;width:212px">Lorem ipsum dolor sit amet, consectetur adipisicing elit, sed do eiusmod tempor incididunt ut labore et dolore magna aliqua.Ut enim ad minim veniam, quis nostrud exercitation ullamco laboris nisi ut aliquip ex ea commodo consequat. Duis aute irure dolor in reprehenderit in voluptate velit esse cillum dolore eu fugiat nulla pariatur. Excepteur sint occaecat</p>
  </section>

  <form class="abs form">
    <h3>Customers Form</h3>
    <p>Lorem ipsum dolor sit amet, consectetur adipisicing elit, sed do eiusmod tempor incididunt .</p>
    <div class="field">Name</div>
    <div class="field" style="margin-top:7px">Email</div>
    <div class="field area">Message</div>
    <div class="submit">Submit Now</div>
  </form>

  <section>
    <h2 class="abs section-title" style="left:97px;top:849px">Blog</h2>
    <div class="abs avatar-warm" style="left:97px;top:873px;width:75px;height:52px" role="img" aria-label="Portrait photo of a smiling woman"></div>
    <div class="abs name" style="left:185px;top:872px">Mara</div>
    <p class="abs body-copy" style="left:185px;top:888px;width:215px">Lorem ipsum dolor sit amet, consectetur adipisicing elit, sed do eiusmod tempor incididunt ut labore et dolore magna aliqua.Ut enim ad minim veniam, quis nostrud exercitation ullamco laboris nisi ut aliquip ex ea commodo consequat. Duis aute irure dolor in reprehenderit in voluptate velit esse.</p>

    <h2 class="abs section-title" style="left:460px;top:849px">Testimonials</h2>
    <div class="abs avatar-cool" style="left:461px;top:872px;width:35px;height:30px" role="img" aria-label="Portrait photo of a smiling man"></div>
    <p class="abs body-copy" style="left:508px;top:870px;width:215px">Lorem ipsum dolor sit amet, consectetur adipisicing elit, sed do eiusmod tempor incididunt ut labore et dolore magna aliqua.Ut enim ad minim veniam, quis nostrud exercitation ullamco laboris nisi ut aliquip ex ea commodo consequat. Duis aute irure dolor in reprehenderit in voluptate velit esse.</p>
    <div class="abs" style="left:560px;top:946px;width:159px;text-align:right;font-size:8.4px;color:var(--ink)"><span style="color:var(--green)">Theo,</span> Lumen Studio</div>
  </section>

  <footer class="abs footer"></footer>
  <div class="abs f-title" style="left:97px;top:1003px">About Us</div>
  <div class="abs f-mark" style="left:125px;top:1034px"></div>
  <div class="abs f-brand" style="left:97px;top:1060px">Bright Harbor Capital</div>
  <p class="abs f-text" style="left:97px;top:1089px;width:192px">Lorem ipsum dolor sit amet, consectetur adipisicing elit, sed do eiusmod tempor incididunt ut labore et dolore magna aliqua. Ut enim ad minim veniam, quis nostrud exercitation.</p>

  <div class="abs f-title" style="left:318px;top:1003px">Navigation</div>
  <ul class="abs f-links" style="left:319px;top:1027px">
    <li>Home</li><li>Funding application</li><li>About our firm</li><li>Partner profiles</li><li>Our process</li><li>Investment profiles</li><li>Contact us</li>
  </ul>

  <div class="abs f-title" style="left:441px;top:1003px">News latter</div>
  <p class="abs f-text" style="left:442px;top:1025px;width:112px;line-height:11.7px">Lorem ipsum dolor sit amet, consectetur adipisicing elit, sed do eiusmod tempor incididunt ut labore et dolore magna aliqua.Ut enim ad minim veniam, quis nostrud exercitation ullamco laboris nisi ut aliquip ex ea</p>

  <div class="abs f-title" style="left:587px;top:1003px">Get in touch</div>
  <div class="abs contact" style="left:587px;top:1025px">
    Telephone:&nbsp;&nbsp; +1 555 010 2040<br>
    Fax:&nbsp;&nbsp;&nbsp; +1 555 010 7788<br>
    E-mail:&nbsp;&nbsp; hello@brightharbor.example<br>
    <span style="display:block;height:13px"></span>
    412 Quay Lane,<br>Porthaven, PH 12 4QL.
  </div>
  <div class="abs f-title" style="left:587px;top:1121px">Interesting stuff</div>
  <div class="abs social foot"><span></span><span></span><span></span><span></span><span></span><span></span><span></span></div>

  <div class="abs footer-bottom">Copyright © 2014 Bright Harbor. All Rights Reserved</div>
</div>
</body>
</html>
```